Brand: Comet Gherkin; watermelon pickle pouch packaging design, flavor: WATERMELON SANDIA

can you design a pouch for a watermelon-flavored pickle, you should be using bold colors and designs, also maybe background could be a slice of watermelon, we want bright colors, and an eye catching design, also maybe have a pickle character on it, i have attached a picture of a pickle pouch for example.. .........................................................................

Target Market(s)

all people, mostly younger people

Industry/Entity Type

pickles, candy

Colors
00AB8E
00BBA5
67D7C9
C6EFE9
E9F9F6
FFF300
FFF600
FEFA6F
FFFEC7
FFFEE8
EB3D1F
EC4F4E
F09395
F8D3D4
FCEDEE
E54698
E96AAD
F1A4CE
F9D9EA
FCEFF6

Requirements
Must have
• bright colors, like bright green and hot pink, and maybe bright yellow, can you please use the same red as the watermelon in the photo attached? the design needs to look juicy and appetizing
Nice to have
• watermelon background like watermelon sliced with the seeds, font of words should be in black bubble letters, and a window
Should not have
• n/a

```html
<!DOCTYPE html>
<html lang="en">
<head>
<meta charset="utf-8">
<title>Comet Gherkin – Watermelon-Flavored Pickle Pouch</title>
<link rel="stylesheet" href="https://fonts.googleapis.com/css2?family=Oswald:wght@500;700&display=swap">
<style>
  :root {
    --teal: #00AB8E;
    --teal-light: #C6EFE9;
    --mint: #67D7C9;
    --yellow: #FFF300;
    --pink: #E54698;
    --pink-soft: #E96AAD;
    --white: #FFFFFF;
    --ink: #000000;
  }
  html, body {
    margin: 0;
    padding: 0;
    overflow: hidden;
    background: var(--white);
  }
  .pouch {
    position: relative;
    width: 700px;
    height: 1200px;
    overflow: hidden;
    font-family: "Oswald", "Arial Narrow", sans-serif;
  }
  .stripe-pattern {
    position: absolute;
    inset: 0;
    background: linear-gradient(90deg, var(--teal) 0%, #3cc3ad 50%, var(--teal) 100%);
  }
  .melon-slice {
    position: absolute;
    background: linear-gradient(180deg, var(--pink) 0%, var(--pink) 80%, var(--mint) 100%);
  }
  .melon-slice--right {
    left: 424px;
    top: 320px;
    width: 276px;
    height: 376px;
    border-radius: 0 0 0 200px;
  }
  .melon-slice--left {
    left: 0;
    top: 600px;
    width: 195px;
    height: 292px;
    border-radius: 0 0 160px 0;
  }
  .brand-name {
    position: absolute;
    left: 0;
    right: 0;
    top: 228px;
    margin: 0;
    text-align: center;
    font-weight: 700;
    font-size: 104px;
    line-height: 0.98;
    letter-spacing: 4px;
    color: var(--ink);
    text-transform: uppercase;
  }
  .window-badge {
    position: absolute;
    left: 0;
    top: 0;
    width: 700px;
    height: 1200px;
  }
  .window-label {
    font-family: "Oswald", "Arial Narrow", sans-serif;
    font-weight: 500;
    font-size: 50px;
    letter-spacing: 6px;
    fill: var(--ink);
  }
  .flavor-line {
    font-family: "Oswald", "Arial Narrow", sans-serif;
    font-weight: 500;
    font-size: 30px;
    fill: var(--ink);
  }
  .net-weight {
    position: absolute;
    right: 30px;
    bottom: 34px;
    margin: 0;
    font-weight: 500;
    font-size: 34px;
    line-height: 1;
    color: var(--ink);
  }
</style>
</head>
<body>
  <main class="pouch">
    <div class="stripe-pattern" role="img" aria-label="Wavy vertical watermelon-rind stripes in dark and pale green"></div>
    <div class="melon-slice melon-slice--right" role="img" aria-label="Illustrated watermelon slice with pink flesh, black seeds and green rind"></div>
    <div class="melon-slice melon-slice--left" role="img" aria-label="Illustrated watermelon slice with pink flesh, black seeds and green rind"></div>

    <h1 class="brand-name">Comet<br>Gherkin</h1>

    <svg class="window-badge" viewBox="0 0 700 1200" aria-hidden="false">
      <defs>
        <radialGradient id="window-shade" cx="350" cy="830" r="260" gradientUnits="userSpaceOnUse">
          <stop offset="0.55" stop-color="#ffffff"/>
          <stop offset="0.85" stop-color="#d9d9d9"/>
          <stop offset="1" stop-color="#7a7a7a"/>
        </radialGradient>
        <path id="flavor-arc" d="M 88 968 Q 350 1100 616 962"/>
      </defs>
      <path class="badge-frame" fill="var(--pink)" stroke="var(--pink)" stroke-width="10" stroke-linejoin="round"
            d="M 350 491 L 641 971 Q 350 1130 59 976 Z"/>
      <path class="badge-band" fill="var(--yellow)"
            d="M 350 519 L 625 965 Q 350 1110 73 968 Z"/>
      <path class="product-window" fill="url(#window-shade)"
            d="M 350 549 L 583 943 Q 350 1052 117 943 Z"/>
      <text class="window-label" x="343" y="852" text-anchor="middle">WINDOW</text>
      <text class="flavor-line">
        <textPath href="#flavor-arc" startOffset="50%" text-anchor="middle" textLength="520" lengthAdjust="spacing">WATERMELON-FLAVORED PICKLE</textPath>
      </text>
    </svg>

    <p class="net-weight">250mg</p>
  </main>
</body>
</html>
```